Box design for toddler shoes

Hi,

TASK:
I need a shoe box designed for our rubber soled socks.

DIMENSION:
13.5cmHx12cmWx7.2cmD

​BOX FEATURE:
1. Must include the following information
a) our logo
b) the product name ‘Rubber Soled Socks’
c) Some product key features that could be written on the box include:
- Indoor and outdoor wear
- Soft and flexible sole
- Light weight and comfortable
d) Sock composition and care instructions also needs to be included on the box,
probably quite small. Maybe on the base.

Sock: 80% Cotton 10% Spandex 10% Polyester
Rubber Sole

Care instructions:
Cold Machine Wash or Hand Wash
Do not bleach
Do not tumble dry

Made in China
Distributed by LW Tots
www.lwtots-sample.com.au

2. A CUT OUT in the lid so you can see at least part of the shoe/sock pattern design. I am open to different size and shape cut outs, but need the shoes to not be at risk of falling out of the box.

DESIGN KEYPOINTS:
1. I would like a modern classic design. I like the yellow shoe box picture attached, but am happy and open for a different design. This just gives you the idea of the fresh look I like.

2. NO brown craft packaging, but am open to options for other colours.

3. NO picture of the socks on the box design
- the CUT on the lid will allow buyer to see the pattern on the socks. Attached is images of the sample shoe/socks that will be put in the boxes and how they will be packaged in the rectangle box. There are many different designs/colour. All will need to be packaged in the same box.

4. I'd love to see what the box would look like as it sits on the shelf, but also need the flat lay design ready for printing.

Please let me know if you have any questions to help with your design.

I can't wait to see your design.

Thanks,
Maren

Industry/Entity Type

Baby/kids

Font styles to use
Sans Serif
Other font styles liked:
• More modern version of Sans Serif

Requirements
Must have
• Cut out in the top of the box so you can see part of the sock to know which design is packaged inside.
Should not have
• Bubble font

```html
<!DOCTYPE html>
<html lang="en">
<head>
<meta charset="utf-8">
<title>Little Wren – Rubber Soled Socks Box</title>
<link href="https://fonts.googleapis.com/css2?family=Montserrat:wght@500;600;700&display=swap" rel="stylesheet">
<style>
  :root {
    --stage: #f1f1f1;
    --box-yellow: #f0b415;
    --tread-light: #fbf3a8;
    --tread-bright: #f6dc1c;
    --paper: #ffffff;
    --window-inside: #e4e1d8;
    --window-edge: #c9c4b6;
    --ink: #2a2a2a;
    --type-light: #ffffff;
  }
  * { margin: 0; padding: 0; box-sizing: border-box; }
  html, body {
    width: 1200px; height: 1200px; overflow: hidden;
    background: var(--stage);
    font-family: "Montserrat", sans-serif;
  }
  .dieline { position: relative; width: 1200px; height: 1200px; }
  .panel {
    position: absolute; left: 100px; width: 1000px;
    background: var(--box-yellow); overflow: hidden;
    box-shadow: 0 2px 10px rgba(0,0,0,0.08);
  }
  .panel-lid { top: 90px; height: 580px; }
  .panel-front { top: 700px; height: 400px; }
  .panel-art { position: absolute; inset: 0; width: 100%; height: 100%; }

  .panel-copy { position: absolute; text-align: center; color: var(--type-light); }
  .panel-lid .panel-copy { left: 500px; right: 30px; top: 40px; }
  .panel-front .panel-copy { left: 480px; right: 20px; top: 60px; }

  .brand-name {
    font-weight: 600; font-size: 60px; letter-spacing: 1px; line-height: 1;
    color: var(--type-light);
  }
  .product-name { font-weight: 700; font-size: 26px; margin-top: 8px; letter-spacing: 0.3px; }
  .panel-front .brand-name { font-size: 74px; }
  .panel-front .product-name { color: var(--ink); font-size: 32px; margin-top: 10px; }

  .feature-list {
    list-style: none; margin-top: 14px; font-weight: 600; font-size: 17px; line-height: 1.55;
  }
  .feature-list li { display: inline-block; margin: 0 6px; }
  .feature-list li:nth-child(3) { display: block; }
  .feature-list li::before {
    content: ""; display: inline-block; width: 12px; height: 12px; border-radius: 50%;
    background: var(--ink); margin-right: 7px; vertical-align: -1px;
  }
  .panel-front .feature-list { color: var(--ink); font-size: 22px; margin-top: 18px; }
  .panel-front .feature-list li::before { width: 15px; height: 15px; }

  .care-info, .composition, .maker-info {
    font-weight: 500; font-size: 15px; line-height: 1.5;
  }
  .care-info { margin-top: 36px; }
  .composition { margin-top: 14px; }
  .maker-info { margin-top: 14px; }
</style>
</head>
<body>
<main class="dieline">

  <section class="panel panel-lid" aria-label="Lid top">
    <svg class="panel-art" viewBox="0 0 1000 580" preserveAspectRatio="none">
      <defs>
        <linearGradient id="lid-tread" x1="0" y1="0" x2="1" y2="0">
          <stop offset="0" stop-color="var(--tread-light)"/>
          <stop offset="0.55" stop-color="var(--tread-bright)"/>
          <stop offset="1" stop-color="var(--box-yellow)"/>
        </linearGradient>
      </defs>
      <path class="paper-field" d="M0 0 H400 C385 200 360 400 340 580 H0 Z" fill="var(--paper)"/>
      <g role="img" aria-label="Bright yellow tyre-track brush texture sweeping along the white edge">
        <path d="M400 0 H540 C505 200 470 400 450 580 H340 C360 400 385 200 400 0 Z" fill="url(#lid-tread)"/>
      </g>
      <g class="lid-window" role="img" aria-label="Die-cut window in the lid showing the sock pattern inside">
        <rect x="70" y="150" width="250" height="280" rx="125" fill="var(--window-inside)" stroke="var(--window-edge)" stroke-width="3"/>
      </g>
    </svg>
    <div class="panel-copy">
      <h1 class="brand-name">Little Wren</h1>
      <p class="product-name">Rubber Soled Socks</p>
      <ul class="feature-list">
        <li>Indoor and outdoor wear</li>
        <li>Soft and flexible sole</li>
        <li>Light weight and comfortable</li>
      </ul>
      <p class="care-info">Care Instructions:<br>Cold Machine Wash or Hand Wash<br>Do not bleach<br>Do not tumble dry</p>
      <p class="composition">Sock: 80% Cotton 10% Spandex 10% Polyester<br>Rubber Sole</p>
      <p class="maker-info">Made in China<br>Distributed by LW Tots<br>www.lwtots-sample.com.au</p>
    </div>
  </section>

  <section class="panel panel-front" aria-label="Front side">
    <svg class="panel-art" viewBox="0 0 1000 400" preserveAspectRatio="none">
      <defs>
        <linearGradient id="front-tread" x1="0" y1="0" x2="1" y2="0">
          <stop offset="0" stop-color="var(--tread-light)"/>
          <stop offset="0.55" stop-color="var(--tread-bright)"/>
          <stop offset="1" stop-color="var(--box-yellow)"/>
        </linearGradient>
      </defs>
      <path class="paper-field" d="M0 0 H380 C365 150 340 290 310 400 H0 Z" fill="var(--paper)"/>
      <g role="img" aria-label="Bright yellow tyre-track brush texture sweeping along the white edge">
        <path d="M380 0 H500 C470 150 430 290 400 400 H310 C340 290 365 150 380 0 Z" fill="url(#front-tread)"/>
      </g>
    </svg>
    <div class="panel-copy">
      <h2 class="brand-name">Little Wren</h2>
      <p class="product-name">Rubber Soled Socks</p>
      <ul class="feature-list">
        <li>Indoor and outdoor wear</li>
        <li>Soft and flexible sole</li>
        <li>Light weight and comfortable</li>
      </ul>
    </div>
  </section>

</main>
</body>
</html>
```